Personal creative Biz Card Design

Need personal yet natural and organic design. The cards I have now are well designed but look too commercial. I want more organic FEELING kind of card. I thought having a headshot would make it more personal... but maybe a sketch effect (or line drawing effect) of face better (?). Maybe in a gray or tungsten color?

Target Market(s)

Well, everyone i give card to will have already seen me face-to-face so that is one thing. Mostly yoga students and people interested in improving their fitness or general health. People looking for wellness, a personal fitness trainer, a yoga teacher

Industry/Entity Type

Health And Wellness

Contact Information for Business Card

I provided examples

Requirements
Must have
• My main logo
• My name

```html
<!DOCTYPE html>
<html lang="en">
<head>
<meta charset="utf-8">
<title>Owen Marlow – Business Card</title>
<link href="https://fonts.googleapis.com/css2?family=Quicksand:wght@500;600;700&display=swap" rel="stylesheet">
<style>
  :root {
    --backdrop: #8c8c8c;
    --card-white: #ffffff;
    --card-dark: #3b3939;
    --leaf-green: #4c9a34;
    --cream: #ecead0;
    --badge-grey: #d9d9d9;
    --badge-grey-dark: #c4c4c4;
    --photo-light: #e9e6e0;
    --photo-mid: #a89a88;
  }
  * { margin: 0; padding: 0; box-sizing: border-box; }
  html, body { width: 1200px; height: 857px; overflow: hidden; }
  body {
    position: relative;
    background: var(--backdrop);
    font-family: "Quicksand", sans-serif;
  }

  /* ---------- Front card ---------- */
  .front-card {
    position: absolute;
    left: 205px; top: 45px;
    width: 560px; height: 330px;
    background: var(--card-white);
    border-radius: 165px 0 0 165px / 165px 0 0 165px;
  }
  .front-card .brand-name {
    position: absolute;
    left: 150px; top: 110px;
    display: flex; align-items: center; gap: 14px;
    font-size: 40px; font-weight: 700;
    color: var(--leaf-green);
    letter-spacing: 0.5px;
  }
  .brand-dot {
    width: 26px; height: 26px; border-radius: 50%;
    background: var(--leaf-green);
    flex: none;
  }
  .partner-badges {
    position: absolute;
    left: 110px; top: 252px;
    display: flex; align-items: center; gap: 24px;
  }
  .partner-badges .badge { background: var(--badge-grey); }
  .badge--wide { width: 62px; height: 26px; border-radius: 4px; }
  .badge--round { width: 40px; height: 40px; border-radius: 50%; background: var(--badge-grey-dark) !important; }
  .badge--long { width: 110px; height: 24px; border-radius: 4px; }

  /* ---------- Back card ---------- */
  .back-card {
    position: absolute;
    left: 400px; top: 395px;
    width: 600px; height: 420px;
  }
  .back-card__shape { position: absolute; inset: 0; }
  .back-card .logo-name {
    position: absolute;
    left: 78px; top: 96px;
    display: flex; align-items: center; gap: 7px;
    font-size: 17px; font-weight: 700;
    color: var(--leaf-green);
  }
  .logo-name .brand-dot { width: 11px; height: 11px; }

  .service-list {
    position: absolute;
    left: 48px; top: 170px;
    list-style: none;
    color: var(--cream);
    font-size: 12.5px; font-weight: 600;
    line-height: 15px;
  }
  .service-list li {
    position: relative;
    padding-left: 14px;
    margin-bottom: 7px;
  }
  .service-list li::before {
    content: "";
    position: absolute; left: 0; top: 5px;
    width: 6px; height: 6px; border-radius: 50%;
    background: var(--cream);
  }
  .divider {
    position: absolute;
    left: 140px; top: 327px;
    width: 66px; height: 2px;
    background: var(--cream);
  }
  .contact-list {
    position: absolute;
    right: 310px; top: 338px;
    list-style: none;
    color: var(--cream);
    font-size: 13.5px; font-weight: 600;
    line-height: 16px;
    text-align: right;
  }
  .contact-list li {
    display: flex; justify-content: flex-end; align-items: center;
    gap: 8px; margin-bottom: 4px;
    white-space: nowrap;
  }
  .contact-icon { width: 16px; height: 16px; flex: none; }

  .portrait {
    position: absolute;
    left: 300px; top: 0;
    width: 300px; height: 300px;
    border-radius: 50%;
    border: 9px solid var(--card-white);
    background: radial-gradient(circle at 45% 40%, var(--photo-mid) 0%, #c9bcab 35%, var(--photo-light) 70%);
  }
</style>
</head>
<body>

  <section class="front-card" aria-label="Business card front">
    <div class="brand-name"><span class="brand-dot"></span>OWEN MARLOW</div>
    <div class="partner-badges" aria-label="Certification badges">
      <span class="badge badge--wide"></span>
      <span class="badge badge--wide"></span>
      <span class="badge badge--round"></span>
      <span class="badge badge--wide"></span>
      <span class="badge badge--long"></span>
    </div>
  </section>

  <section class="back-card" aria-label="Business card back">
    <svg class="back-card__shape" width="600" height="420" viewBox="0 0 600 420">
      <rect x="0" y="70" width="450" height="340" fill="var(--card-dark)"/>
      <polygon points="0,88 320,70 320,128 0,158" fill="var(--card-white)"/>
    </svg>

    <div class="logo-name"><span class="brand-dot"></span>OWEN MARLOW</div>

    <ul class="service-list">
      <li>Teacher of Yoga</li>
      <li>Leader of Yoga Teacher Trainings</li>
      <li>Personal Fitness Trainer</li>
      <li>Private &amp; public classes/sessions</li>
      <li>Nutrition, Wellness, Meditation,<br>Healing ceremonies (puja &amp; shamanic)</li>
      <li>Certified &amp; Insured</li>
    </ul>

    <span class="divider"></span>

    <ul class="contact-list">
      <li>555-210-4387
        <svg class="contact-icon" viewBox="0 0 16 16"><circle cx="8" cy="8" r="7" fill="none" stroke="var(--cream)" stroke-width="1.2"/><path d="M5.5 4.5l1.5 0 .6 2-1 .8a5 5 0 0 0 2 2l.8-1 2 .6v1.5c-3.8.5-6.5-2.2-6-5.9z" fill="var(--cream)"/></svg>
      </li>
      <li>owenstillpaths@mail.com
        <svg class="contact-icon" viewBox="0 0 16 16"><circle cx="8" cy="8" r="7" fill="none" stroke="var(--cream)" stroke-width="1.2"/><rect x="4.5" y="5.5" width="7" height="5" fill="none" stroke="var(--cream)" stroke-width="1"/><path d="M4.5 5.5l3.5 3 3.5-3" fill="none" stroke="var(--cream)" stroke-width="1"/></svg>
      </li>
      <li>www.owenmarlow.com
        <svg class="contact-icon" viewBox="0 0 16 16"><circle cx="8" cy="8" r="7" fill="none" stroke="var(--cream)" stroke-width="1.2"/><circle cx="8" cy="8" r="3.6" fill="none" stroke="var(--cream)" stroke-width="1"/><path d="M4.4 8h7.2M8 4.4v7.2" stroke="var(--cream)" stroke-width="1"/></svg>
      </li>
    </ul>

    <div class="portrait" role="img" aria-label="Headshot portrait of the yoga teacher in a white shirt"></div>
  </section>

</body>
</html>
```